Gentleman's grooming products require a business card

I need a business card that incorporates the logo [ or parts of ] that we had Art Parade design for us as uploaded.

We sell online, mens grooming products including moustache waxes, beard oils and shaving accessories.
We want a card that is classy, professional and a card that shouts mens products.

Target Market(s)

Young professional male market

Industry/Entity Type

Business

Contact Information for Business Card

Tess and Dulcie Abbott
Brass and Bristle
Purveyors of gentleman's stiffeners and grooming requisites
M :0491527306
E : tess@brassandbristle.com.au
E : dulcie@brassandbristle.com.au
E : sales@theboulevardpomade.com.au

W : www.brassandbristle.com.au

Requirements
Must have
• Class
Nice to have
• Professionalism

```html
<!DOCTYPE html>
<html lang="en">
<head>
<meta charset="utf-8">
<title>Brass and Bristle — Business Card</title>
<link rel="stylesheet" href="https://fonts.googleapis.com/css2?family=Cinzel:wght@400&family=Open+Sans:wght@400;700&display=swap">
<style>
  :root {
    --backdrop: #3a322d;
    --card: #0d0d0d;
    --card-edge: #1c1c1c;
    --ink: #f2f2f2;
    --silver: #c9c9c9;
    --silver-dim: #8d8d8d;
    --divider: #3a3a3a;
  }
  * { box-sizing: border-box; margin: 0; padding: 0; }
  html, body { width: 1200px; height: 900px; overflow: hidden; }
  body {
    background: var(--backdrop);
    font-family: "Open Sans", Arial, sans-serif;
    position: relative;
  }
  .card {
    position: absolute;
    top: 295px;
    width: 530px;
    height: 310px;
    background: var(--card);
    border: 1px solid var(--card-edge);
    border-radius: 3px;
  }
  .card--contact { left: 55px; }
  .card--brand { left: 615px; }

  /* Contact side */
  .brand-mark {
    position: absolute;
    left: 40px;
    top: 100px;
    width: 150px;
    display: flex;
    flex-direction: column;
    align-items: center;
    gap: 12px;
  }
  .brand-mark__square {
    width: 70px;
    height: 70px;
    background: var(--ink);
  }
  .brand-mark__name {
    font-family: "Cinzel", Georgia, serif;
    font-size: 15px;
    color: var(--ink);
    text-align: center;
    line-height: 1.2;
  }
  .contact {
    position: absolute;
    left: 220px;
    top: 62px;
  }
  .contact__name {
    font-weight: 700;
    font-size: 17px;
    line-height: 24px;
    color: var(--ink);
    margin-bottom: 8px;
  }
  .contact__list {
    list-style: none;
    margin-left: -14px;
    padding-left: 14px;
    border-left: 1px solid var(--divider);
  }
  .contact__item {
    display: flex;
    align-items: center;
    gap: 10px;
    font-size: 15px;
    color: var(--ink);
    line-height: 23px;
    white-space: nowrap;
  }
  .contact__icon { width: 11px; height: 11px; flex: none; fill: var(--ink); }

  /* Brand side */
  .brand {
    position: absolute;
    inset: 0;
    display: flex;
    flex-direction: column;
    align-items: center;
    justify-content: center;
    gap: 12px;
  }
  .brand__name {
    font-family: "Cinzel", Georgia, serif;
    font-size: 44px;
    color: var(--silver);
    letter-spacing: 1px;
  }
  .brand__tagline {
    font-family: "Cinzel", Georgia, serif;
    font-size: 10.5px;
    letter-spacing: 1.6px;
    color: var(--silver-dim);
    text-transform: uppercase;
    white-space: nowrap;
  }
</style>
</head>
<body>
  <section class="card card--contact">
    <div class="brand-mark">
      <div class="brand-mark__square"></div>
      <div class="brand-mark__name">Brass and Bristle</div>
    </div>
    <div class="contact">
      <h1 class="contact__name">Tess and Dulcie Abbott</h1>
      <ul class="contact__list">
        <li class="contact__item">
          <svg class="contact__icon" viewBox="0 0 12 12"><rect x="3" y="0" width="6" height="12" rx="1"/><rect x="4" y="1.5" width="4" height="7.5" fill="#0d0d0d"/></svg>
          0491527306
        </li>
        <li class="contact__item">
          <svg class="contact__icon" viewBox="0 0 12 12"><rect x="0" y="2" width="12" height="8"/><path d="M0.5 2.5 L6 7 L11.5 2.5" stroke="#0d0d0d" stroke-width="1.2" fill="none"/></svg>
          tess@brassandbristle.com.au
        </li>
        <li class="contact__item">
          <svg class="contact__icon" viewBox="0 0 12 12"><rect x="0" y="2" width="12" height="8"/><path d="M0.5 2.5 L6 7 L11.5 2.5" stroke="#0d0d0d" stroke-width="1.2" fill="none"/></svg>
          dulcie@brassandbristle.com.au
        </li>
        <li class="contact__item">
          <svg class="contact__icon" viewBox="0 0 12 12"><rect x="0" y="2" width="12" height="8"/><path d="M0.5 2.5 L6 7 L11.5 2.5" stroke="#0d0d0d" stroke-width="1.2" fill="none"/></svg>
          sales@theboulevardpomade.com.au
        </li>
        <li class="contact__item">
          <svg class="contact__icon" viewBox="0 0 12 12"><circle cx="6" cy="6" r="6"/><path d="M0 6 H12 M6 0 V12 M6 0 C2.5 3 2.5 9 6 12 M6 0 C9.5 3 9.5 9 6 12" stroke="#0d0d0d" stroke-width="0.9" fill="none"/></svg>
          www.brassandbristle.com.au
        </li>
      </ul>
    </div>
  </section>

  <section class="card card--brand">
    <div class="brand">
      <div class="brand__name">Brass and Bristle</div>
      <div class="brand__tagline">Suppliers of fine moustache waxes and gentlemen's provisions</div>
    </div>
  </section>
</body>
</html>
```